Design a single page Shopify store web page

We are looking to have a page designed for a single page Shopify store with 2 products. We already have a basic structure that we like, though we are open to suggestions. We are looking for somebody to provide a design/color scheme that we can then implement using Shopify's templating system. We can handle the implementation(HTML / CSS / jS) as we already have 2 web developers on the team, but have not been able to find a design we liked.

The job would consist of providing a mockup (photoshop or otherwise) and any vector graphics you choose to create for the site (we can provide product photos and other images).

You can also look at http://brickwellgoods.com.au for some of our design direction we have used so far

Target Market(s)

Young Australian Males (18 - 49)

Industry/Entity Type

Store

Number of Pages Required

1 page

Font styles to use
Serif
Sans Serif

Requirements
Must have
• Single Page Design
• E-commerce Product Purchase
• Manly (whatever interpretation of that you have)

```html
<!DOCTYPE html>
<html lang="en">
<head>
<meta charset="utf-8">
<title>Brickwell Goods – Underwear &amp; Socks Delivered</title>
<link rel="stylesheet" href="https://fonts.googleapis.com/css2?family=Anton&family=Arimo:wght@400;700&family=Changa+One&display=swap">
<style>
:root{
  --ink:#1e1e1e;
  --header:#1b1b1b;
  --navy:#0b2a6e;
  --navy-deep:#061a4a;
  --yellow:#f4e631;
  --green:#6aae0c;
  --green-dark:#4b8a06;
  --faq-green:#76b000;
  --blue:#3e8bd0;
  --light:#ececec;
  --panel:#4d4d4d;
  --circle-dark:#2d2d2d;
  --footer:#2b2b2b;
  --white:#ffffff;
  --rule:#d9d9d9;
  --photo-light:#d3d3d3;
  --photo-dark:#2a3556;
}
*{margin:0;padding:0;box-sizing:border-box}
html,body{width:1200px;height:3279px;overflow:hidden}
body{font-family:"Arimo",Arial,sans-serif;color:var(--ink);background:var(--white);position:relative}
section,header,footer{position:absolute;left:0;width:1200px}
.abs{position:absolute}

/* header */
.site-header{top:0;height:81px;background:var(--header)}
.brand{left:92px;top:24px;display:flex;align-items:center;gap:10px;color:var(--white);font-weight:700;font-size:26px;line-height:30px}
.brand-square{width:24px;height:24px;background:var(--green)}
.nav-link{top:31px;color:var(--white);font-size:15px;text-decoration:none;white-space:nowrap}
.signup{left:981px;top:28px;width:112px;height:26px;background:var(--green);color:var(--white);font-size:13px;font-weight:700;line-height:26px;text-align:center;clip-path:polygon(0 0,100% 0,92% 50%,100% 100%,0 100%,6% 50%)}

/* hero */
.hero{top:81px;height:468px;background:linear-gradient(180deg,var(--navy),var(--navy-deep));overflow:hidden}
.hero-line{left:105px;font-family:"Anton",Impact,sans-serif;color:var(--white);text-transform:uppercase;letter-spacing:1.5px;line-height:1;white-space:nowrap}
.hero-line.l1{top:46px;font-size:62px}
.hero-line.l2{top:126px;font-size:50px}
.hero-line.l3{top:196px;font-size:52px;color:var(--yellow)}
.hero-btn{left:107px;top:299px;width:297px;height:64px;background:linear-gradient(180deg,#7cc619,var(--green-dark));border:2px solid #9ad93a;border-radius:4px;color:var(--white);font-family:"Changa One",sans-serif;font-size:38px;line-height:58px;text-align:center;letter-spacing:1px}
.hero-photo{left:808px;top:0;width:274px;height:468px;background:linear-gradient(180deg,#2c3a6e 0%,#243268 100%)}
.dots{top:414px;left:572px;display:flex;gap:6px}
.dots span{width:14px;height:14px;border-radius:50%;background:var(--white)}
.dots span.on{background:var(--green)}

/* section titles */
.sec-title{left:0;width:1200px;text-align:center;font-size:40px;font-weight:400}
.rule{height:10px;border-top:3px solid var(--rule);border-bottom:3px solid var(--rule)}

/* how it works */
.how{top:549px;height:489px;background:var(--white)}
.how .sec-title{top:46px}
.how .sec-title em{font-style:normal;color:var(--green)}
.step-circle{width:176px;height:176px;border-radius:50%;background:var(--white);box-shadow:0 3px 8px rgba(0,0,0,.18);text-align:center;padding-top:46px;color:#555}
.step-circle.active{background:var(--circle-dark);color:var(--white)}
.step-circle h4{font-size:16px;font-weight:400;margin-bottom:10px}
.step-circle p{font-size:10px;line-height:13px;padding:0 32px}
.step-title{width:340px;text-align:center;font-size:28px;font-weight:400}
.step-text{width:340px;text-align:center;font-size:12.5px;line-height:18px;color:#333}

/* about */
.about{top:1038px;height:455px;background:var(--blue);color:var(--white)}
.about .sec-title{top:50px}
.about .rule{border-color:#6aa6dd}
.col{width:320px;text-align:center}
.col h3{font-size:28px;font-weight:400;line-height:31px;margin-bottom:12px}
.col p{font-size:13px;line-height:20px;padding:0 20px}

/* plans */
.plans{top:1493px;height:1036px;background:var(--light)}
.plans .sec-title{top:54px}
.plan-label{font-size:28px;width:240px;text-align:center}
.plan-photo{width:269px;height:269px;background:var(--white);border:1px solid #d4d4d4;padding:30px}
.plan-photo div{width:100%;height:100%}
.bar{width:135px;height:44px;background:var(--panel)}
.price{font-size:48px;font-weight:700;color:var(--ink)}
.price span{color:var(--green)}
.get-btn{width:133px;height:40px;background:var(--green-dark);border-radius:3px;color:var(--white);font-size:24px;line-height:40px;padding-left:12px;display:flex;align-items:center;gap:10px}
.features{left:87px;top:597px;width:1017px;height:66px;background:var(--white);border-bottom:3px solid #555}
.feature{top:21px;font-size:17px;display:flex;align-items:center;gap:10px}
.insta-title{top:705px;left:0;width:1200px;text-align:center;font-size:40px;font-weight:400}
.insta-tile{top:785px;width:175px;height:175px;background:var(--panel)}

/* faq */
.faq{top:2529px;height:625px;background:var(--faq-green);color:var(--white)}
.faq .sec-title{top:46px}
.faq .rule{border-color:#93c63a}
.faq .col p{font-size:12.5px;line-height:19px}
.faq .divider{height:5px;border-top:2px solid #93c63a;border-bottom:2px solid #93c63a;width:280px}
.mail{color:var(--yellow)}

/* footer */
.site-footer{top:3154px;height:125px;background:var(--footer);color:var(--white);font-size:13px}
.social{top:50px;left:672px;display:flex;gap:12px;font-size:12px}
.social span{display:flex;align-items:center;gap:4px}
.social i{width:10px;height:10px;background:#6aa6dd;display:inline-block}
.cards{top:48px;left:936px;display:flex;gap:10px}
.cards span{width:50px;height:30px;border-radius:4px;background:#d9d9d9}
</style>
</head>
<body>

<header class="site-header">
  <div class="brand abs"><span class="brand-square"></span>Brickwell Goods</div>
  <a class="nav-link abs" style="left:555px">How it works</a>
  <a class="nav-link abs" style="left:693px">About Us</a>
  <a class="nav-link abs" style="left:811px">Plans</a>
  <a class="nav-link abs" style="left:898px">FAQ</a>
  <div class="signup abs">Sign Up Now!</div>
</header>

<section class="hero">
  <div class="hero-line l1 abs">New Underwear and Socks</div>
  <div class="hero-line l2 abs">Delivered to your door</div>
  <div class="hero-line l3 abs">Every 3 or &nbsp;6 Month</div>
  <div class="hero-btn abs">YES PLEASE !</div>
  <div class="hero-photo abs" role="img" aria-label="Photo of a model wearing the store's trunks"></div>
  <div class="dots abs"><span></span><span class="on"></span><span></span></div>
</section>

<section class="how">
  <div class="rule abs" style="left:142px;top:63px;width:335px"></div>
  <div class="rule abs" style="left:728px;top:63px;width:339px"></div>
  <h2 class="sec-title abs">How it <em>works</em></h2>

  <div class="step-circle abs" style="left:190px;top:128px"><h4>Lorem Ipsum</h4><p>Lorem Ipsum has been the industry's standard dummy text ever</p></div>
  <div class="step-circle active abs" style="left:513px;top:128px"><h4>Lorem Ipsum</h4><p>Lorem Ipsum has been the industry's standard dummy text ever</p></div>
  <div class="step-circle abs" style="left:845px;top:128px"><h4>Lorem Ipsum</h4><p>Lorem Ipsum has been the industry's standard dummy text ever</p></div>

  <h3 class="step-title abs" style="left:108px;top:322px">Choose a Plan</h3>
  <p class="step-text abs" style="left:108px;top:361px">There will be plans for all budgets and styles</p>
  <h3 class="step-title abs" style="left:431px;top:322px">Choose How Often</h3>
  <p class="step-text abs" style="left:431px;top:361px">Decide whether you would like to receive<br>new packages every 3 or 6 months</p>
  <h3 class="step-title abs" style="left:763px;top:322px">Get your Pack</h3>
  <p class="step-text abs" style="left:763px;top:361px">We'll send out your first pack right away<br>and then again every 3 or 6 months</p>
</section>

<section class="about">
  <div class="rule abs" style="left:171px;top:70px;width:327px"></div>
  <div class="rule abs" style="left:700px;top:70px;width:327px"></div>
  <h2 class="sec-title abs">About Us</h2>
  <div class="col abs" style="left:122px;top:165px"><h3>What is your<br>cancellation policy?</h3><p>You can cancel any time you want There are no contracts and no fees. Just sign into your account and cancel your subscription.</p></div>
  <div class="col abs" style="left:445px;top:165px"><h3 style="margin-bottom:30px">What about sizing?</h3><p>Brickwell Goods stocks all the same brands that you know and love and thankfully underwear are elastic. Just order your normal size and you'll be fine.</p></div>
  <div class="col abs" style="left:784px;top:165px"><h3>How Does Payment<br>Work?</h3><p>You credit card will be charged when you place your order. For ongoing plans you will be automatically charged again when subsequent packages are shipped.</p></div>
</section>

<section class="plans">
  <div class="rule abs" style="left:198px;top:73px;width:335px"></div>
  <div class="rule abs" style="left:678px;top:73px;width:335px"></div>
  <h2 class="sec-title abs">Plans</h2>

  <div class="plan-label abs" style="left:195px;top:192px">COMFORT</div>
  <div class="plan-photo abs" style="left:120px;top:251px"><div role="img" aria-label="Product photo of the Comfort plan underwear" style="background:var(--photo-light)"></div></div>
  <div class="bar abs" style="left:409px;top:251px"></div>
  <div class="bar abs" style="left:409px;top:304px"></div>
  <div class="price abs" style="left:468px;top:372px"><span>$</span>30</div>
  <div class="get-btn abs" style="left:409px;top:439px">GET IT!
    <svg width="18" height="18" viewBox="0 0 18 18"><circle cx="9" cy="9" r="9" fill="#fff"/><path d="M7 5l4 4-4 4" stroke="#4b8a06" stroke-width="2.4" fill="none"/></svg></div>

  <div class="plan-label abs" style="left:757px;top:192px">STYLE</div>
  <div class="plan-photo abs" style="left:654px;top:251px"><div role="img" aria-label="Product photo of the Style plan socks" style="background:var(--photo-dark)"></div></div>
  <div class="bar abs" style="left:944px;top:251px"></div>
  <div class="bar abs" style="left:944px;top:304px"></div>
  <div class="price abs" style="left:1003px;top:372px"><span>$</span>30</div>
  <div class="get-btn abs" style="left:944px;top:439px">GET IT!
    <svg width="18" height="18" viewBox="0 0 18 18"><circle cx="9" cy="9" r="9" fill="#fff"/><path d="M7 5l4 4-4 4" stroke="#4b8a06" stroke-width="2.4" fill="none"/></svg></div>

  <div class="features abs">
    <div class="feature abs" style="left:31px"><svg width="30" height="26" viewBox="0 0 30 26"><path d="M3 14l8 8L27 3" stroke="#4fa10d" stroke-width="6" fill="none"/></svg>Free Shipping</div>
    <div class="feature abs" style="left:280px"><svg width="30" height="26" viewBox="0 0 30 26"><path d="M3 14l8 8L27 3" stroke="#4fa10d" stroke-width="6" fill="none"/></svg>Easy Returns</div>
    <div class="feature abs" style="left:510px"><svg width="30" height="26" viewBox="0 0 30 26"><path d="M3 14l8 8L27 3" stroke="#4fa10d" stroke-width="6" fill="none"/></svg>Cancel Whenever</div>
    <div class="feature abs" style="left:772px"><svg width="30" height="26" viewBox="0 0 30 26"><path d="M3 14l8 8L27 3" stroke="#4fa10d" stroke-width="6" fill="none"/></svg>Satisfaction Gaurante</div>
  </div>

  <h2 class="insta-title abs">What's up on our Snapgrid?</h2>
  <div class="insta-tile abs" style="left:85px"></div>
  <div class="insta-tile abs" style="left:296px"></div>
  <div class="insta-tile abs" style="left:507px"></div>
  <div class="insta-tile abs" style="left:718px"></div>
  <div class="insta-tile abs" style="left:929px"></div>
</section>

<section class="faq">
  <div class="rule abs" style="left:198px;top:64px;width:335px"></div>
  <div class="rule abs" style="left:678px;top:64px;width:335px"></div>
  <h2 class="sec-title abs">FAQ</h2>

  <div class="col abs" style="left:89px;top:165px"><h3 style="margin-bottom:32px">What is Brickwell Goods?</h3><p>Brickwell Goods is an Australian subscription service for mens underwear and socks. We stock all your favourite brands and have a range of plans for all budgets and styles.</p></div>
  <div class="col abs" style="left:452px;top:150px"><h3>What is your<br>Satisfaction Guarantee?</h3><p>We consider Brickwell Goods to be a premium service and customer service is key to that. If for any reason you aren't satisfied simply return your package for a full refund of the charge. In the case of a recurring packages we'll refund the most recent charge.</p></div>
  <div class="col abs" style="left:780px;top:165px"><h3 style="margin-bottom:32px">Shipping Policy</h3><p>Shipping if FREE Australia wide. We ship all of our packages within 48 hours of payment Monday-Friday. All our packs are shipped through Southern Parcel Post with tracking.</p></div>

  <div class="divider abs" style="left:114px;top:378px"></div>
  <div class="divider abs" style="left:472px;top:378px"></div>
  <div class="divider abs" style="left:800px;top:378px"></div>

  <div class="col abs" style="left:89px;top:410px"><h3>What do I get with my<br>Brickwell Plan?</h3><p>You'll get 3 pairs of underwear and 3 pairs of socks. You select the frequency of deliveries when you sign up.</p></div>
  <div class="col abs" style="left:452px;top:424px"><h3>Returns Policy</h3><p>We have a 30 days returns policy. To be eligible for a return, You item must be unused and in the same condition that you received it. If you need to make a return simply email <span class="mail">holla@brickwellgoods.com.au</span></p></div>
  <div class="col abs" style="left:780px;top:410px"><h3>What Brands do you<br>Stock?</h3><p>Brickwell Goods currently stock Harbour Knit, Stockman, Carlton Reed, Tidewater Co and Quiet Ox. Is your favourite brand missing? Let us know <span class="mail">holla@brickwellgoods.com.au</span></p></div>
</section>

<footer class="site-footer">
  <div class="abs" style="left:87px;top:52px">Shissing / Returns / Payment / Terms / Privacy</div>
  <div class="abs" style="left:448px;top:56px">holla@brickwellgoods.com.au</div>
  <div class="social abs">
    <span><i></i>Facepage</span><span><i></i>Chirp</span><span><i></i>Blogr</span><span><i></i>Snapgrid</span>
  </div>
  <div class="cards abs"><span></span><span></span><span></span></div>
</footer>

</body>
</html>
```